Flyer for "Master the Mash Tun Basics" course

NEEDED: A6 flyer designed to advertise my first training course:
Intro to craft beer brewing

The company brand identity was recently bought from Pixel Harbor and it can be seen, with colour scheme on our website: www.TinmoorKettle.com.

The flyer is to be in line with my current brand identity and have a strong hook to push people to our site.

The flyer's goal is to get people to visit the site to book on a craft beer brewing training course. The info available to be included, although you have the freedom to include as much or as little as you see fit:

Currently a sale of 60% off on the course cost
RRP £120 Sale Price £50 (limited time only)
Courses will be run in central London
The website is TinmoorKettle.com
Hands on, half day course, brunch and a couple of sample beers included
Dates available:
14th December 2014
11th January 2015
18th January 2015
25th January 2015
1st February 2015
8th February 2015
15th February 2015
22nd February 2015

Logo file included, AI version available on request. Any photo on the TinmoorKettle.com site is available to be used. Simply pull of the site or I can send to you.

Colour scheme used on site: #FF9700 & #26210D

I will reply to any designs offered between 8pm and 11pm BST each day.

Good luch!

Hi everyone, We have now reviewed the first submissions and there are some ok, some good and a couple of great efforts in there. Here are the following common things that we commented on in our first reviews: 1. WHAT IS THE FLYER TRYING TO SAY... YOU'VE GOT 1 SECOND!!!! This flyer is to be given out in the street. That gives you 1second to tell the reader what the flyer is selling. That is the number 1 priority for the flyer. Please make it your priority as designers. 2. SALE SALE SALE This is the number 2 priority, people love SALES and a big colourful sticker saying SALE or 60% OFF (or both) is to be positioned so once the reader has seen that the flyer is about a craft beer brewing course, they see there is a sale on the course. 3. BRAND PERSONALITY 3rd priority is the Tinmoor Kettle brand identity. We picked this name, logo and colour scheme to stand out. Please use these to enhance points 1 & 2, but also get our logo on there is a bold and brash way. 4. USE THE BACK OF THE CARD Place any info that is not required in 1, 2 & 3 on the back, or even remove it all together if YOU feel it is not suited. You are the designer, so make some design decisions! We are happy to ask you to add things back in if we feel it is lacking. Our best guess (and we are NOT designers) is that putting either the dates OR a brief description of the course on the back would be enough info. If you think we can get bother, without overloading the page, give it a go! 5. CALL TO ACTION On the front and on the back, we want a CALL TO ACTION. Book at TinmoorKettle.com or just TinmoorKettle.com (you do not need http://www before it!!! We live in 2014 not 1994!!!) 6. MAKE IT BOLD, & THEN MAKE IT BOLDER This flyer is to stand out to a person that is handed 1 different leaflet every 2 minutes while walking down a busy London high street. We MUST stand out. Finally, thanks for all the designer so far, your efforts are greatly appreciated and we are very excited about the new revision of the design!

Target Market(s)

City living, young professionals who like to do fun things at the weekend.

Industry/Entity Type

Training

Font styles to use
Sans Serif

Colors
f78f20

Requirements
Must have
• Strong brand identity and call to action
In line with brand identity, see website www.TinmoorKettle.com

```html
<!DOCTYPE html>
<html lang="en">
<head>
<meta charset="utf-8">
<title>Tinmoor Kettle – Brewing Course Flyer</title>
<link rel="stylesheet" href="https://fonts.googleapis.com/css2?family=Oswald:wght@500;600;700&family=Roboto+Condensed:wght@400;700&display=swap">
<style>
  :root {
    --orange: #f78f20;
    --dark: #26210d;
    --paper: #ffffff;
    --photo-street-top: #b7a58e;
    --photo-street-bottom: #5e5346;
    --photo-group-top: #c9b9a4;
    --photo-group-bottom: #6d6053;
  }
  * { box-sizing: border-box; margin: 0; padding: 0; }
  html, body { width: 847px; height: 1200px; overflow: hidden; background: var(--paper); }
  .flyer {
    position: relative; width: 847px; height: 1200px; overflow: hidden;
    background: var(--dark);
    font-family: "Roboto Condensed", Arial, sans-serif;
    color: var(--dark);
  }
  .venue-photo {
    position: absolute; left: 0; top: 0; width: 100%; height: 640px;
    background: linear-gradient(170deg, var(--photo-street-top), var(--photo-street-bottom));
  }
  .location-note {
    position: absolute; left: 0; top: 0; width: 100%; height: 32px;
    background: var(--dark); color: var(--paper);
    font-size: 15px; line-height: 32px; padding-left: 14px;
  }
  .course-title {
    position: absolute; left: 300px; top: 70px; width: 300px;
    font-family: "Oswald", Arial, sans-serif; font-weight: 700; font-size: 58px;
    line-height: 1.02; color: var(--paper); text-transform: uppercase;
  }
  .course-title span { color: var(--orange); }
  .sale-sticker {
    position: absolute; left: 618px; top: 70px; width: 200px; height: 200px;
    border-radius: 50%; background: var(--orange); border: 6px solid var(--dark);
    display: flex; flex-direction: column; align-items: center; justify-content: center;
    font-family: "Oswald", Arial, sans-serif; color: var(--dark); text-transform: uppercase;
  }
  .sale-label { font-size: 30px; font-weight: 600; line-height: 1; }
  .sale-amount { font-size: 64px; font-weight: 700; line-height: 1; }
  .sale-price { font-family: "Roboto Condensed", Arial, sans-serif; font-size: 20px; font-weight: 700; margin-top: 4px; text-transform: none; }
  .brand-block {
    position: absolute; left: 0; top: 402px; width: 273px; height: 207px;
    background: var(--orange);
    display: flex; flex-direction: column; align-items: center; justify-content: center; gap: 12px;
  }
  .brand-dot { width: 84px; height: 84px; border-radius: 50%; background: var(--dark); }
  .brand-name {
    font-family: "Oswald", Arial, sans-serif; font-weight: 600; font-size: 30px;
    color: var(--dark); text-transform: uppercase; text-align: center; line-height: 1.05;
  }
  .content-tab {
    position: absolute; left: 0; top: 609px; width: 410px; height: 57px;
    background: var(--dark); color: var(--paper);
    font-family: "Oswald", Arial, sans-serif; font-weight: 600; font-size: 36px;
    line-height: 57px; padding-left: 30px; text-transform: uppercase;
  }
  .content-panel {
    position: absolute; left: 0; top: 666px; width: 488px; height: 402px;
    background: var(--orange); padding: 10px 16px 0 22px;
  }
  .content-intro { font-size: 30px; line-height: 1.15; margin-bottom: 6px; }
  .content-list { list-style: none; }
  .content-list li { font-size: 30px; line-height: 1.18; padding-left: 34px; position: relative; }
  .content-list li::before {
    content: ""; position: absolute; left: 4px; top: 12px; width: 14px; height: 14px;
    background: var(--dark); transform: rotate(45deg);
  }
  .hook-box {
    position: absolute; left: 502px; top: 637px; width: 339px; height: 224px;
    background: var(--paper); border: 5px solid var(--orange);
    font-size: 30px; line-height: 1.16; padding: 14px 16px; color: var(--dark);
  }
  .group-photo {
    position: absolute; left: 502px; top: 876px; width: 339px; height: 216px;
    background: linear-gradient(160deg, var(--photo-group-top), var(--photo-group-bottom));
  }
  .web-band {
    position: absolute; left: 0; top: 1105px; width: 100%; height: 95px;
    background: var(--orange);
    display: flex; align-items: center; padding-left: 70px; gap: 60px;
  }
  .web-address { font-size: 58px; color: var(--dark); }
</style>
</head>
<body>
<main class="flyer">
  <div class="venue-photo" role="img" aria-label="Photo of the pub venue on a cobbled street with hanging flower baskets"></div>
  <p class="location-note">Our prime location is 10 minutes walk from Kings Cross, London in a wonderful free house, Marlowe's.</p>

  <h1 class="course-title">Craft Beer <span>Brewing</span> Course</h1>
  <div class="sale-sticker">
    <span class="sale-label">Sale</span>
    <span class="sale-amount">60%</span>
    <span class="sale-label">Off</span>
    <span class="sale-price">Now £50</span>
  </div>

  <div class="brand-block">
    <span class="brand-dot"></span>
    <span class="brand-name">Tinmoor<br>Kettle</span>
  </div>

  <h2 class="content-tab">Course Content</h2>
  <section class="content-panel">
    <p class="content-intro">The course covers all areas of brewing beer for the novice or the startup commercial brewer alike:</p>
    <ul class="content-list">
      <li>Brewing equipment</li>
      <li>Water treatment</li>
      <li>Malts, body &amp; alcohol</li>
      <li>Mashing &amp; Sparging</li>
      <li>Hops, bitterness &amp; aroma</li>
      <li>Boiling &amp; cooling</li>
      <li>Fermenting</li>
    </ul>
  </section>

  <p class="hook-box">Want to learn how barley and hops turn into the world's most important liquid?</p>

  <div class="group-photo" role="img" aria-label="Photo of course attendees holding sample beers"></div>

  <footer class="web-band">
    <svg class="mouse-icon" width="44" height="64" viewBox="0 0 44 64" aria-hidden="true">
      <rect x="3" y="3" width="38" height="58" rx="19" fill="none" stroke="#26210d" stroke-width="4"/>
      <line x1="22" y1="3" x2="22" y2="24" stroke="#26210d" stroke-width="4"/>
      <line x1="3" y1="24" x2="41" y2="24" stroke="#26210d" stroke-width="4"/>
    </svg>
    <span class="web-address">TinmoorKettle.com</span>
  </footer>
</main>
</body>
</html>
```